Langmore Plumbing Heating and Electric

We are looking for a basic, but very beautiful and professional looking website. We would like the ability for a customer to request service through our website via a form or email that will be forwarded to us. Other then that just contact info, our history, our rates, and the services we offer.

Look at his page, it is WAY TOO BASIC, but if gives a very general base line idea: http://www.dialfenwickpipes.example/

http://www.pipequarry.example/norfolk/?cmpid=10000&keyword=plumbing

http://www.valvewick-williamsburg.example/emergency_plumbing.html?keyphrase=emergency+plumbing+services

Target Market(s)

Heating, air conditioning, plumbing, natural gas

Industry/Entity Type

Plumbing

Number of Pages Required

4 page

Requirements
Must have
• Professional looking, very high end and modern,
Nice to have
• Would like the ability for client to contact us for service through the website utilizing some type of email.

```html
<!DOCTYPE html>
<html lang="en">
<head>
<meta charset="utf-8">
<title>Company Name | Plumbing and Drain Cleaning</title>
<link rel="stylesheet" href="https://fonts.googleapis.com/css2?family=Source+Sans+3:ital,wght@0,400;0,600;0,700;1,600&family=Open+Sans:wght@400&display=swap">
<style>
  :root {
    --page-bg: #ffffff;
    --band-grey: #e6e6e6;
    --teal: #8eb0b2;
    --brand-dark: #3d4a4c;
    --maroon: #4a1717;
    --button-red: #9a1d1d;
    --text-body: #2e2e2e;
    --rule: #c8c8c8;
    --footer-text: #555555;
    --white: #ffffff;
  }
  * { box-sizing: border-box; margin: 0; padding: 0; }
  html, body { width: 900px; height: 1200px; overflow: hidden; }
  body {
    background: var(--page-bg);
    font-family: "Source Sans 3", "Helvetica Neue", Arial, sans-serif;
    color: var(--text-body);
    position: relative;
  }

  .site-header {
    position: absolute; left: 0; top: 0; width: 900px; height: 144px;
    background: var(--band-grey);
  }
  .brand {
    position: absolute; left: 52px; top: 50px;
    display: flex; align-items: center; gap: 14px;
  }
  .brand-mark { width: 26px; height: 26px; background: var(--brand-dark); }
  .brand-name {
    font-size: 30px; font-weight: 700; color: var(--brand-dark); letter-spacing: -0.5px;
  }

  .contact-bar {
    position: absolute; left: 0; top: 144px; width: 900px; height: 45px;
    background: var(--teal); color: var(--white);
  }
  .contact-email {
    position: absolute; left: 55px; top: 0; height: 45px;
    display: flex; align-items: center; gap: 16px; font-size: 20px;
  }
  .contact-phone {
    position: absolute; right: 57px; top: 0; height: 45px;
    display: flex; align-items: center; gap: 14px; font-size: 29px;
  }

  .hero {
    position: absolute; left: 0; top: 189px; width: 900px; height: 465px;
    border-bottom: 6px solid var(--maroon);
  }
  .hero-photo {
    position: absolute; inset: 0;
    background: linear-gradient(100deg, #6f655a 0%, #9e927f 30%, #b5a996 55%, #8f8576 80%, #a39b91 100%);
  }
  .hero-copy {
    position: absolute; right: 358px; top: 108px; text-align: right; color: var(--white);
    text-shadow: 0 1px 3px rgba(0,0,0,0.35);
  }
  .hero-title {
    font-size: 30px; font-weight: 700; line-height: 35px; letter-spacing: -0.8px;
  }
  .hero-points { list-style: none; margin-top: 27px; }
  .hero-points li {
    font-size: 28px; font-style: italic; font-weight: 600; letter-spacing: -0.9px;
    line-height: 35px; display: flex; justify-content: flex-end; align-items: center; gap: 10px;
  }
  .hero-points svg { flex: none; }

  .schedule-panel {
    position: absolute; left: 586px; top: 54px; width: 273px; height: 333px;
    background: rgba(225,225,225,0.93); border-radius: 4px; overflow: hidden;
  }
  .schedule-head {
    height: 73px; background: var(--white);
    display: flex; align-items: center; gap: 12px; padding-left: 13px;
    font-size: 24px; color: #3a3a3a;
  }
  .schedule-form { padding: 24px 9px 0; }
  .field {
    height: 32px; margin-bottom: 20px; display: flex;
    background: var(--white); border: 1px solid #cfcfcf;
  }
  .field span {
    flex: 1; padding-left: 11px; line-height: 30px; font-size: 17px; color: #b5b5b5;
  }
  .field i {
    width: 27px; background: #e4e4e4; border-left: 1px solid #bbb;
    display: flex; align-items: center; justify-content: center;
  }
  .schedule-button {
    display: block; width: 255px; height: 52px; margin-top: 2px;
    background: var(--button-red); color: var(--white); border: 1px solid #6e1010;
    font-family: inherit; font-size: 24px; border-radius: 2px;
  }

  .section { position: absolute; left: 54px; width: 790px; }
  .section-title {
    font-size: 29px; font-weight: 600; color: var(--maroon);
    padding-left: 3px; padding-bottom: 4px; border-bottom: 2px solid var(--rule);
  }
  .history { top: 667px; }
  .history p { font-size: 14.2px; line-height: 17.2px; font-weight: 600; color: #3a3a3a; margin-top: 9px; }
  .history p + p { margin-top: 0; }

  .rates { top: 900px; }
  .rates-grid {
    display: grid; grid-template-columns: 454px 1fr; margin-top: 7px; padding-left: 4px;
  }
  .rate { display: flex; align-items: baseline; height: 21px; }
  .rate b { width: 99px; font-size: 18.5px; font-weight: 700; color: #3a3a3a; }
  .rate strong { font-size: 18.5px; font-weight: 600; color: #3a3a3a; }
  .rate small { font-size: 11.5px; margin-left: 4px; color: #3a3a3a; }

  .site-footer {
    position: absolute; left: 0; top: 1056px; width: 900px; height: 144px;
    background: var(--band-grey);
    font-family: "Open Sans", Arial, sans-serif;
  }
  .footer-links { position: absolute; top: 18px; list-style: none; }
  .footer-links li { font-size: 16px; line-height: 23.5px; color: var(--footer-text); }
</style>
</head>
<body>
  <header class="site-header">
    <div class="brand">
      <span class="brand-mark"></span>
      <span class="brand-name">Company Name</span>
    </div>
  </header>

  <div class="contact-bar">
    <div class="contact-email">
      <svg width="37" height="26" viewBox="0 0 37 26" aria-hidden="true">
        <rect x="1" y="1" width="35" height="24" fill="none" stroke="#fff" stroke-width="2"/>
        <path d="M1 1 L18.5 15 L36 1 M1 25 L14 12 M36 25 L23 12" fill="none" stroke="#fff" stroke-width="2"/>
      </svg>
      <span>contact@yourcompany.com</span>
    </div>
    <div class="contact-phone">
      <svg width="32" height="32" viewBox="0 0 24 24" aria-hidden="true">
        <path fill="#fff" d="M6.6 10.8c1.4 2.8 3.8 5.1 6.6 6.6l2.2-2.2c.3-.3.7-.4 1-.2 1.1.4 2.3.6 3.6.6.6 0 1 .4 1 1V20c0 .6-.4 1-1 1C10.6 21 3 13.4 3 4c0-.6.4-1 1-1h3.5c.6 0 1 .4 1 1 0 1.3.2 2.5.6 3.6.1.3 0 .7-.2 1z"/>
      </svg>
      <span>555.555.5555</span>
    </div>
  </div>

  <section class="hero">
    <div class="hero-photo" role="img" aria-label="Photo of a bright, elegant bathroom with a window view"></div>
    <div class="hero-copy">
      <h1 class="hero-title">Full Service Plumbing and<br>Drain Cleaning</h1>
      <ul class="hero-points">
        <li>Free Estimates <svg width="30" height="26" viewBox="0 0 30 26" aria-hidden="true"><path d="M2 14 L11 23 L28 3" fill="none" stroke="#fff" stroke-width="6" stroke-linejoin="round"/></svg></li>
        <li>Open 24 Hours, 7 Days a Week <svg width="30" height="26" viewBox="0 0 30 26" aria-hidden="true"><path d="M2 14 L11 23 L28 3" fill="none" stroke="#fff" stroke-width="6" stroke-linejoin="round"/></svg></li>
        <li>Trusted &amp; Recommended Since 19XX <svg width="30" height="26" viewBox="0 0 30 26" aria-hidden="true"><path d="M2 14 L11 23 L28 3" fill="none" stroke="#fff" stroke-width="6" stroke-linejoin="round"/></svg></li>
      </ul>
    </div>

    <form class="schedule-panel">
      <div class="schedule-head">
        <svg width="30" height="30" viewBox="0 0 30 30" aria-hidden="true">
          <rect x="1" y="4" width="28" height="25" fill="#444"/>
          <rect x="6" y="0" width="4" height="7" fill="#444"/><rect x="20" y="0" width="4" height="7" fill="#444"/>
          <g fill="#fff">
            <rect x="4" y="11" width="4" height="3"/><rect x="10" y="11" width="4" height="3"/><rect x="16" y="11" width="4" height="3"/><rect x="22" y="11" width="4" height="3"/>
            <rect x="4" y="17" width="4" height="3"/><rect x="10" y="17" width="4" height="3"/><rect x="16" y="17" width="4" height="3"/><rect x="22" y="17" width="4" height="3"/>
            <rect x="4" y="23" width="4" height="3"/><rect x="10" y="23" width="4" height="3"/><rect x="16" y="23" width="4" height="3"/><rect x="22" y="23" width="4" height="3"/>
          </g>
        </svg>
        <span>Schedule Service</span>
      </div>
      <div class="schedule-form">
        <div class="field"><span>DD/MM/YYYY</span><i><svg width="11" height="8" viewBox="0 0 11 8" aria-hidden="true"><path d="M0 0 H11 L5.5 8Z" fill="#222"/></svg></i></div>
        <div class="field"><span>Time</span><i><svg width="11" height="8" viewBox="0 0 11 8" aria-hidden="true"><path d="M0 0 H11 L5.5 8Z" fill="#222"/></svg></i></div>
        <div class="field"><span>Service Type</span><i><svg width="11" height="8" viewBox="0 0 11 8" aria-hidden="true"><path d="M0 0 H11 L5.5 8Z" fill="#222"/></svg></i></div>
        <button type="button" class="schedule-button">Schedule Service</button>
      </div>
    </form>
  </section>

  <section class="section history">
    <h2 class="section-title">Our History</h2>
    <p>Aperum aut enit dit aut enis ape dolorro mos molupie nimolupta elissun dionsequi nobis as ne re autes aut debis unt, nus aboriae voles endis molorenimi, simene quo molut quibusd aectesequia arci tetus minveles atumquamus eribusaero que libus qui que sin rero eatint asimet lame quam fugitias eos que dolupturis dolorrorem quunte officium ilis repta volupta si ab im diat.</p>
    <p>Modio cus et ate excea veruntio officia nderfereic tet voluptatur aliquib usciden isquunt.</p>
    <p>Busdae sant faciat. Ex enis quis molor maiosaerem quatur?</p>
    <p>Itat. Quiam qui veliquiaspis at andam exceprat evenet elent volupta voluptaque re et earum quibus moditatus volese conseriamet etur, seque nati abo. Tint lanis consequias doloremporum suntia paribero ducient, cus acerum res aut lati berum eostibu sandig-nate net laut illacestem intinis rehenetus si officae vendi aut ditatuste nullaboritio eatento te consed quaero quis deria si que volupta atiorrori ne ese resed qui comnihi llautes sequiant facepta pedicae sin ea comnis verspit, conectaquia cum fugite ipsam, voluptatem volenestem de reius ditiis ab imus rent.</p>
  </section>

  <section class="section rates">
    <h2 class="section-title">Rates</h2>
    <div class="rates-grid">
      <div>
        <div class="rate"><b>Job Type 1</b><strong>$ 40</strong><small>+taxes &amp; fees</small></div>
        <div class="rate"><b>Job Type 2</b><strong>$ 65</strong><small>+taxes &amp; fees</small></div>
        <div class="rate"><b>Job Type 3</b><strong>$ 100</strong><small>+taxes &amp; fees</small></div>
        <div class="rate"><b>Job Type 4</b><strong>$ 150</strong><small>+taxes &amp; fees</small></div>
      </div>
      <div>
        <div class="rate"><b>Job Type 5</b><strong>$ 175</strong><small>+taxes &amp; fees</small></div>
        <div class="rate"><b>Job Type 6</b><strong>$ 200</strong><small>+taxes &amp; fees</small></div>
        <div class="rate"><b>Job Type 7</b><strong>$ 300</strong><small>+taxes &amp; fees</small></div>
        <div class="rate"><b>Job Type 8</b><strong>$ 500+</strong><small>+taxes &amp; fees</small></div>
      </div>
    </div>
  </section>

  <footer class="site-footer">
    <ul class="footer-links" style="left:54px">
      <li>Home</li><li>Careers</li><li>Plumbing Basics</li>
    </ul>
    <ul class="footer-links" style="left:319px">
      <li>Schedule Service</li><li>Residential Plumbing</li><li>Commercial Plumbing</li><li>Pipe Cleaning</li>
    </ul>
    <ul class="footer-links" style="left:643px">
      <li>Products</li><li>Contact Us</li><li>About Us</li><li>Privacy Policy</li>
    </ul>
  </footer>
</body>
</html>
```